Prepare a modern, professional business card for Bramford Ledger Services (BLS) Our company is in the banking, compliance and finance industry. We provide kiosks, software integration, and compliance guidelines so that banks can "bank" Marijuana Dispensaries with TrevMon, Office of Halvern Affairs and NTRB approval.

Target Market(s)

Banks

Industry/Entity Type

Business

Contact Information for Business Card

Owen R Pelley
Bramford Ledger Services
Vice President
742 Quarry Ridge Road
Suite 310
Las Vegas, NV 89135
owen@bramfordls.net
702-555-0147

Font styles to use
Sans Serif

Requirements
Nice to have
• I like the clean simple appearance of Quillon computers. Perhaps the three LETTERS of BLS can be the LOGO on the Card and the Company name could be incorporated in the contact information. Like colors of white, black and gray

```html
<!DOCTYPE html>
<html lang="en">
<head>
<meta charset="utf-8">
<title>Bramford Ledger Services – Business Card</title>
<link href="https://fonts.googleapis.com/css2?family=Ubuntu:wght@400;500;700&display=swap" rel="stylesheet">
<style>
  :root {
    --page-bg: #ecebe8;
    --card-face: #d8d7d0;
    --card-frame: #4d4e4a;
    --frame-line: #9a9a94;
    --ink: #2b2b29;
    --ink-soft: #56554f;
    --mark: #58564f;
    --mark-faint: rgba(88, 86, 79, 0.16);
    --divider: #6b6a64;
  }
  * { box-sizing: border-box; margin: 0; padding: 0; }
  html, body {
    width: 1200px;
    height: 1000px;
    overflow: hidden;
    background: var(--page-bg);
    font-family: "Ubuntu", sans-serif;
  }
  .business-card {
    position: absolute;
    left: 110px;
    top: 220px;
    width: 980px;
    height: 560px;
    background: var(--card-frame);
    padding: 18px;
    box-shadow: 0 10px 30px rgba(0,0,0,0.18);
  }
  .card-face {
    position: relative;
    width: 100%;
    height: 100%;
    background: var(--card-face);
    outline: 2px solid var(--frame-line);
    outline-offset: -10px;
    overflow: hidden;
  }
  .brand-block {
    position: absolute;
    left: 40px;
    top: 150px;
    width: 400px;
    text-align: center;
  }
  .brand-initials {
    font-size: 110px;
    font-weight: 700;
    letter-spacing: 2px;
    color: var(--mark);
    line-height: 1;
  }
  .brand-name {
    margin-top: 12px;
    font-size: 17px;
    font-weight: 700;
    letter-spacing: 1px;
    text-transform: uppercase;
    color: var(--mark);
  }
  .column-divider {
    position: absolute;
    left: 462px;
    top: 60px;
    width: 2px;
    height: 360px;
    background: var(--divider);
  }
  .contact-block {
    position: absolute;
    left: 500px;
    top: 62px;
    color: var(--ink);
  }
  .person-name {
    font-size: 36px;
    font-weight: 700;
    line-height: 1.1;
  }
  .person-role {
    font-size: 23px;
    color: var(--ink-soft);
    margin-top: 6px;
  }
  .contact-row {
    display: flex;
    align-items: flex-start;
    gap: 14px;
    font-size: 23px;
    line-height: 1.5;
    color: var(--ink);
    margin-top: 6px;
  }
  .contact-row svg { flex: none; margin-top: 5px; }
  .faint-mark {
    position: absolute;
    right: 10px;
    bottom: -40px;
    font-size: 180px;
    font-weight: 700;
    color: var(--mark-faint);
    line-height: 1;
  }
</style>
</head>
<body>
  <div class="business-card">
    <div class="card-face">
      <div class="brand-block">
        <div class="brand-initials">BLS</div>
        <div class="brand-name">Bramford Ledger Services</div>
      </div>

      <div class="column-divider"></div>

      <div class="contact-block">
        <div class="person-name">Owen R Pelley</div>
        <div class="person-role">Vice President</div>

        <div class="contact-row">
          <svg width="24" height="24" viewBox="0 0 24 24" aria-hidden="true">
            <circle cx="12" cy="12" r="12" fill="#2b2b29"/>
            <path d="M12 5a4.5 4.5 0 0 0-4.5 4.5c0 3.4 4.5 9 4.5 9s4.5-5.6 4.5-9A4.5 4.5 0 0 0 12 5z" fill="#d8d7d0"/>
            <circle cx="12" cy="9.5" r="1.7" fill="#2b2b29"/>
          </svg>
          <div>Bramford Ledger Services,<br>742 Quarry Ridge Road,<br>Suite 310,<br>Las Vegas, NV 89135</div>
        </div>

        <div class="contact-row">
          <svg width="24" height="24" viewBox="0 0 24 24" aria-hidden="true">
            <circle cx="12" cy="12" r="12" fill="#2b2b29"/>
            <rect x="6" y="8" width="12" height="9" rx="1" fill="#d8d7d0"/>
            <path d="M6.5 8.5 12 13l5.5-4.5" stroke="#2b2b29" stroke-width="1.3" fill="none"/>
          </svg>
          <div>owen@bramfordls.net</div>
        </div>

        <div class="contact-row">
          <svg width="24" height="24" viewBox="0 0 24 24" aria-hidden="true">
            <circle cx="12" cy="12" r="12" fill="#2b2b29"/>
            <path d="M8.5 6.5l2 2.2-1.3 1.6c.8 1.7 2 2.9 3.6 3.7l1.6-1.3 2.2 2-1.2 1.8c-4-.4-7.4-3.8-7.8-7.8z" fill="#d8d7d0"/>
          </svg>
          <div>702-555-0147</div>
        </div>
      </div>

      <div class="faint-mark" aria-hidden="true">BLS</div>
    </div>
  </div>
</body>
</html>
```